Clearwater Trial Sciences Bi-Fold Brochure

Contract Research Organization for Clinical Research Trial Management

Industry/Entity Type

Pharmaceutical

Font styles to use
Serif
Sans Serif

Colors
34a7d8
3176b5
f68d4d
faa54b

```html
<!DOCTYPE html>
<html lang="en">
<head>
<meta charset="utf-8">
<title>Clearwater Trial Sciences – Bi-Fold Brochure</title>
<link rel="stylesheet" href="https://fonts.googleapis.com/css2?family=Open+Sans:wght@400;600;700&display=swap">
<style>
:root{
  --sky:#34a7d8;
  --blue:#3176b5;
  --navy:#1f5b9e;
  --orange:#f68d4d;
  --amber:#faa54b;
  --gold:#f3c33a;
  --paper:#f8f9fb;
  --paper-shade:#e9edf2;
  --backdrop:#ebebeb;
  --ink:#56616d;
  --rule:#c9d2dc;
}
*{box-sizing:border-box;margin:0;padding:0}
html,body{width:1200px;height:2469px;overflow:hidden}
body{background:var(--backdrop);font-family:"Open Sans",Arial,sans-serif;color:var(--ink);position:relative}

.cover-sheet{position:absolute;left:350px;top:70px;width:500px;height:680px}
.spread{position:absolute;left:130px;width:940px;height:640px;display:flex;box-shadow:0 18px 30px rgba(0,0,0,.12)}
.spread--outer{top:850px}
.spread--inner{top:1620px}
.spread .page{width:470px;height:640px}
.cover-sheet{box-shadow:0 18px 30px rgba(0,0,0,.12)}

.page{position:relative;overflow:hidden;container-type:inline-size;background:var(--paper)}
.page-art{position:absolute;inset:0;width:100%;height:100%;display:block}
.page--left{box-shadow:inset -14px 0 18px -14px rgba(0,0,0,.18)}
.page--right{box-shadow:inset 14px 0 18px -14px rgba(0,0,0,.18)}

.brand-lockup{position:absolute;left:0;right:0;display:flex;align-items:center;justify-content:center;gap:2cqw}
.brand-dot{width:4.6cqw;height:4.6cqw;border-radius:50%;background:var(--orange);flex:none}
.brand-name{font-weight:700;color:var(--blue);font-size:5.4cqw;letter-spacing:-.02em;white-space:nowrap}
.cover-lockup{top:60%}

.cover-tagline{position:absolute;top:70%;left:9%;right:9%;display:flex;align-items:center;gap:3cqw;color:var(--orange);font-weight:600;font-size:3.6cqw;white-space:nowrap}
.cover-tagline::before,.cover-tagline::after{content:"";flex:1;height:2px;background:var(--blue);opacity:.8}

.back-lockup{top:75%;left:10%;right:auto;justify-content:flex-start}
.back-lockup .brand-name{font-size:4cqw}
.back-lockup .brand-dot{width:3.4cqw;height:3.4cqw}
.contact-row{position:absolute;left:5%;right:5%;top:89%;display:flex;justify-content:space-between;font-size:2.1cqw;color:var(--orange)}
.contact-item{display:flex;align-items:center;gap:1.2cqw}
.contact-item svg{width:2.6cqw;height:2.6cqw}

.inner-title{position:absolute;top:7%;left:7%;width:50%;color:var(--orange);font-size:4.2cqw;font-weight:600;line-height:1.25}
.section-heading{position:absolute;color:var(--blue);font-size:3.6cqw;font-weight:600}
.services-heading{top:35%;left:8%}
.about-heading{top:29%;left:12%}

.service-card{position:absolute;left:6%;width:88%;display:flex;align-items:center;gap:3cqw}
.service-card--one{top:41%}
.service-card--two{top:57%}
.service-card--three{top:74%}
.service-icon{width:6.4cqw;height:6.4cqw;border-radius:50%;background:var(--blue);display:flex;align-items:center;justify-content:center;flex:none}
.service-icon svg{width:3.6cqw;height:3.6cqw}
.text-box{flex:1;background:rgba(255,255,255,.8);border:1px solid var(--rule);border-radius:1cqw;padding:2cqw 3cqw;box-shadow:0 1px 3px rgba(0,0,0,.06)}
.bullets{list-style:none;font-size:2.05cqw;line-height:1.6}
.bullets li{position:relative;padding-left:2.4cqw}
.bullets li::before{content:"";position:absolute;left:0;top:.7em;width:1cqw;height:1cqw;border-radius:50%;background:var(--blue)}

.about-box{position:absolute;top:35%;left:10%;width:80%}
.mission-box{position:absolute;top:58%;left:10%;width:80%;display:flex;gap:2cqw;align-items:flex-start}
.mission-box .quote-mark{color:var(--blue);font-size:7cqw;font-weight:700;line-height:.8}
.mission-box p{font-size:2.1cqw;line-height:1.6}
.inner-lockup{top:84%;left:auto;right:8%;justify-content:flex-end}
.inner-lockup .brand-name{font-size:3.4cqw}
.inner-lockup .brand-dot{width:2.8cqw;height:2.8cqw}
</style>
</head>
<body>

<!-- Front cover -->
<section class="cover-sheet page" aria-label="Brochure front cover">
  <svg class="page-art" viewBox="0 0 500 680" preserveAspectRatio="none" aria-hidden="true">
    <defs>
      <linearGradient id="bluefield" x1="0" y1="0" x2="1" y2="1"><stop offset="0" stop-color="#2b6fb0"/><stop offset="1" stop-color="#3f8fcf"/></linearGradient>
      <linearGradient id="paperfield" x1="0" y1="0" x2="0" y2="1"><stop offset="0" stop-color="#eef1f5"/><stop offset="1" stop-color="#fbfcfd"/></linearGradient>
      <linearGradient id="orangeswoosh" x1="0" y1="0" x2="1" y2="0"><stop offset="0" stop-color="#faa54b"/><stop offset="1" stop-color="#f07a2e"/></linearGradient>
    </defs>
    <rect width="500" height="680" fill="url(#paperfield)"/>
    <path d="M0 205 C160 170 360 190 500 360 V395 C400 250 230 200 0 240 Z" fill="url(#orangeswoosh)"/>
    <path d="M0 0 H500 V350 C360 180 170 160 0 195 Z" fill="url(#bluefield)"/>
    <path d="M0 198 C170 165 360 185 500 354" fill="none" stroke="#fff" stroke-width="4"/>
    <rect y="668" width="500" height="12" fill="var(--blue)"/>
  </svg>
  <div class="brand-lockup cover-lockup"><span class="brand-dot"></span><span class="brand-name">Clearwater Trial Sciences</span></div>
  <div class="cover-tagline">Pharmaceutical Research CRO</div>
</section>

<!-- Outer spread: back cover + front cover -->
<section class="spread spread--outer" aria-label="Brochure outer spread">
  <div class="page page--left">
    <svg class="page-art" viewBox="0 0 500 680" preserveAspectRatio="none" aria-hidden="true">
      <defs><linearGradient id="goldswoosh" x1="0" y1="0" x2="1" y2="0"><stop offset="0" stop-color="#f3c33a"/><stop offset="1" stop-color="#faa54b"/></linearGradient></defs>
      <rect width="500" height="680" fill="url(#paperfield)"/>
      <path d="M0 240 C160 205 340 185 500 180 V250 C330 265 150 310 0 395 Z" fill="url(#goldswoosh)"/>
      <path d="M0 0 H500 V176 C330 182 160 200 0 236 Z" fill="url(#bluefield)"/>
      <path d="M0 238 C160 202 330 182 500 178" fill="none" stroke="#fff" stroke-width="4"/>
      <rect y="668" width="500" height="12" fill="var(--blue)"/>
    </svg>
    <div class="brand-lockup back-lockup"><span class="brand-dot"></span><span class="brand-name">Clearwater Trial Sciences</span></div>
    <div class="contact-row">
      <span class="contact-item"><svg viewBox="0 0 16 16"><rect x="1" y="3" width="14" height="10" rx="1" fill="none" stroke="currentColor" stroke-width="1.6"/><path d="M1 4l7 5 7-5" fill="none" stroke="currentColor" stroke-width="1.6"/></svg>hello@clearwatertrials.com</span>
      <span class="contact-item"><svg viewBox="0 0 16 16"><path d="M4 1l3 3-2 2c1 2 3 4 5 5l2-2 3 3-2 3C7 15 1 9 1 3z" fill="currentColor"/></svg>1-800-555-0142</span>
      <span class="contact-item"><svg viewBox="0 0 16 16"><circle cx="8" cy="8" r="6.5" fill="none" stroke="currentColor" stroke-width="1.6"/><path d="M1.5 8h13M8 1.5c-3 3.5-3 9.5 0 13M8 1.5c3 3.5 3 9.5 0 13" fill="none" stroke="currentColor" stroke-width="1.2"/></svg>www.clearwatertrials.com</span>
    </div>
  </div>
  <div class="page page--right">
    <svg class="page-art" viewBox="0 0 500 680" preserveAspectRatio="none" aria-hidden="true">
      <rect width="500" height="680" fill="url(#paperfield)"/>
      <path d="M0 205 C160 170 360 190 500 360 V395 C400 250 230 200 0 240 Z" fill="url(#orangeswoosh)"/>
      <path d="M0 0 H500 V350 C360 180 170 160 0 195 Z" fill="url(#bluefield)"/>
      <path d="M0 198 C170 165 360 185 500 354" fill="none" stroke="#fff" stroke-width="4"/>
      <rect y="668" width="500" height="12" fill="var(--blue)"/>
    </svg>
    <div class="brand-lockup cover-lockup"><span class="brand-dot"></span><span class="brand-name">Clearwater Trial Sciences</span></div>
    <div class="cover-tagline">Pharmaceutical Research CRO</div>
  </div>
</section>

<!-- Inner spread: services + about -->
<section class="spread spread--inner" aria-label="Brochure inner spread">
  <div class="page page--left">
    <svg class="page-art" viewBox="0 0 500 680" preserveAspectRatio="none" aria-hidden="true">
      <rect width="500" height="680" fill="url(#paperfield)"/>
      <path d="M0 0 H500 V130 C330 150 160 185 0 225 Z" fill="url(#bluefield)"/>
      <path d="M0 228 C160 188 330 152 500 133" fill="none" stroke="var(--gold)" stroke-width="5"/>
      <rect y="668" width="500" height="12" fill="var(--blue)"/>
    </svg>
    <h2 class="inner-title">Pharmaceutical Research CRO</h2>
    <h3 class="section-heading services-heading">Our Services</h3>
    <div class="service-card service-card--one">
      <span class="service-icon"><svg viewBox="0 0 16 16"><rect x="2" y="9" width="3" height="5" fill="#fff"/><rect x="6.5" y="6" width="3" height="8" fill="#fff"/><rect x="11" y="3" width="3" height="11" fill="#fff"/></svg></span>
      <div class="text-box"><ul class="bullets">
        <li>Niche CRO specializing in emerging pharmaceutical and biotech companies</li>
        <li>Expedited FDA approval process</li>
        <li>Cost containment</li>
        <li>Quick Study Start Up</li>
      </ul></div>
    </div>
    <div class="service-card service-card--two">
      <span class="service-icon"><svg viewBox="0 0 16 16"><path d="M8 1a5 5 0 0 0-5 5c0 4 5 9 5 9s5-5 5-9a5 5 0 0 0-5-5z" fill="#fff"/><circle cx="8" cy="6" r="2" fill="var(--blue)"/></svg></span>
      <div class="text-box"><ul class="bullets">
        <li>Robust network of pre-qualified clinical research sites</li>
        <li>Over 200,000 research able patients throughout seven states</li>
        <li>Expert Trial Monitoring</li>
        <li>Cutting edge, custom Clinical Trial Management Software</li>
      </ul></div>
    </div>
    <div class="service-card service-card--three">
      <span class="service-icon"><svg viewBox="0 0 16 16"><path d="M2 8.5l4 4 8-9" fill="none" stroke="#fff" stroke-width="2.4"/></svg></span>
      <div class="text-box"><ul class="bullets">
        <li>Comprehensive regulatory administration</li>
        <li>Quick and accurate data management</li>
        <li>Total outsourced approach to project management</li>
      </ul></div>
    </div>
  </div>
  <div class="page page--right">
    <svg class="page-art" viewBox="0 0 500 680" preserveAspectRatio="none" aria-hidden="true">
      <rect width="500" height="680" fill="url(#paperfield)"/>
      <path d="M0 150 C170 125 340 100 500 55 V95 C340 135 170 165 0 185 Z" fill="url(#orangeswoosh)"/>
      <path d="M0 0 H500 V60 C340 105 170 130 0 155 Z" fill="url(#bluefield)"/>
      <path d="M0 157 C170 132 340 107 500 62" fill="none" stroke="#fff" stroke-width="4"/>
      <rect y="668" width="500" height="12" fill="var(--blue)"/>
    </svg>
    <h3 class="section-heading about-heading">About Us</h3>
    <div class="text-box about-box"><ul class="bullets">
      <li>Over 10 years of research experience</li>
      <li>Successfully delivered over 150 trials</li>
      <li>Proven track record in phase I to IV studies</li>
      <li>Dedicated team of certified clinical managers</li>
      <li>Nationwide network of partner research sites</li>
    </ul></div>
    <div class="text-box mission-box">
      <span class="quote-mark">&ldquo;</span>
      <p>Our mission is to provide efficient and reliable research solutions, helping sponsors bring safe and effective treatments to patients faster.</p>
    </div>
    <div class="brand-lockup inner-lockup"><span class="brand-dot"></span><span class="brand-name">Clearwater Trial Sciences</span></div>
  </div>
</section>

</body>
</html>
```